Video Learning Web Application Site Design

We are a new company that produce and distribute educational videos using a subscription model on our website. The videos are streamed on our website and users can tailor their own course packages by creating playlists. Each video-lesson are also split into several smaller segments, and it should be easy to find and play those segments.

Please note that both the screenshots and wireframes provided are only how it looks right now, if you as the designer have a better idea on how to present it then please share it.
Updates

Please view the screenshots as well, I believe I forgot to include two buttons on the wireframes that should be on the Our Courses page. Also, there is no need to make a carbon copy of the wireframes/screenshots, I'd like you designers to come up with a better way of displaying the information if possible. For inspiration you can look at sites like ClipNest (I like the simplicity of their design) and to some extent the Prism UI where they divide different areas of the page into clear "zones".

Thanks,

Reason: I have to extend the deadline because I've been really ill the last week. Will go through the current submissions now and provide feedback and looking forward to more submissions.

Target Market(s)

College and University students. Professionals wanting to expand their knowledge and people that want to learn new skills to get a promotion/new job.

Industry/Entity Type

Tailor

Requirements
Must have
• Must include the logo from the file "brightleaf-logo".
• Should include two pages, one of the video-player page and one of the course list.
• Try to incorporate the colors from the logo.
• Please note: If you look at the video-player.png file just below "Starte Tavla, bruke..." there are two rows, those are sub-parts of the lesson. Both these and the main lesson itself must have some easy way to Play and Add to Playlist.
Nice to have
• We prefer flat design, with simple and clean icons. Don't overdo the colors, stay within 3-4 colors with variations of them.
Should not have
• 3D-like elements, lot of shadows or hard to ready text.

```html
<!DOCTYPE html>
<html lang="en">
<head>
<meta charset="utf-8">
<title>brightleaf – Our Courses</title>
<link href="https://fonts.googleapis.com/css2?family=Roboto:wght@300;400;500;700&display=swap" rel="stylesheet">
<style>
:root{
  --blue:#0b7fb6;
  --blue-dark:#0a6a98;
  --orange:#f5a623;
  --slate:#3c4352;
  --ink:#4a4a4a;
  --muted:#8a8a8a;
  --line:#d6d6d6;
  --panel:#f0f0f0;
  --page:#f3f3f3;
  --white:#ffffff;
}
*{box-sizing:border-box;margin:0;padding:0}
html,body{width:1200px;height:762px;overflow:hidden}
body{font-family:"Roboto",sans-serif;background:var(--page);color:var(--ink);position:relative}

.topbar{position:absolute;left:0;top:0;width:1200px;height:68px;background:var(--white);border-top:1px solid var(--line);border-bottom:1px solid var(--line)}
.brand{position:absolute;left:28px;top:14px;display:flex;align-items:center;gap:10px}
.brand-mark{width:38px;height:38px;border-radius:50%;background:var(--blue)}
.brand-name{font-size:32px;font-weight:500;color:var(--blue);letter-spacing:-0.5px;line-height:38px}
.search{position:absolute;left:265px;top:23px;width:345px;height:26px;border:1px solid #c9c9c9;border-radius:2px;background:var(--white);box-shadow:inset 0 1px 2px rgba(0,0,0,.06);font-size:10px;color:#9a9a9a;padding:8px 8px}
.search svg{position:absolute;right:8px;top:6px}
.account{position:absolute;top:23px;height:26px;border:1px solid #c9c9c9;border-radius:2px;background:var(--white);display:flex;align-items:center;font-size:9.5px;color:#333}
.account .label{padding:0 9px}
.account .label a{color:var(--blue);text-decoration:none}
.account .icon{width:26px;height:24px;border-left:1px solid #c9c9c9;display:flex;align-items:center;justify-content:center}
.account.user{left:898px;width:181px}
.account.logout{left:1093px;width:79px}

.sidebar{position:absolute;left:0;top:68px;width:228px;height:694px;background:var(--white);border-right:3px solid var(--blue)}
.nav-head{height:47px;background:var(--panel);border-bottom:1px solid var(--line);display:flex;align-items:center;padding-left:24px;gap:9px;font-size:14.5px;font-weight:500;color:var(--blue)}
.nav-head .bullet{width:27px;height:27px;border-radius:50%;background:var(--blue);display:flex;align-items:center;justify-content:center}
.nav-head.active{background:var(--blue);color:var(--white)}
.nav-head.active .bullet{background:var(--white)}
.nav-item{height:37.5px;border-bottom:1px solid var(--line);padding-left:58px;font-size:10.5px;color:#666;display:flex;align-items:center}
.nav-item.current{color:var(--blue)}

.content{position:absolute;left:254px;top:68px;width:918px}
.page-title{margin-top:24px;font-size:20px;font-weight:500;color:var(--blue)}
.category{margin-top:17px;font-size:12.5px;color:#666;padding-bottom:5px;border-bottom:2px solid #c2c2c2}
.category + .course{margin-top:13px}
.course{position:relative;height:145px;margin-left:1px;background:var(--white);border:1px solid #cfcfcf;margin-bottom:13px}
.course-thumb{position:absolute;left:17px;top:17px;width:183px;height:108px;border:1px solid #c8d3df;background:linear-gradient(165deg,#dbe7f5 0%,#e9f0e2 45%,#d6e6c6 70%,#f1d9dc 100%)}
.course-body{position:absolute;left:217px;top:19px;right:70px}
.course-title{font-size:12.5px;font-weight:700;color:var(--blue);margin-bottom:7px}
.course-text{font-size:9.6px;line-height:14px;color:#8b8b8b}
.course-stats{position:absolute;right:-1px;top:-1px;width:48px;height:145px;display:flex;flex-direction:column}
.stat{flex:1;display:flex;flex-direction:column;align-items:center;justify-content:center;gap:4px;color:var(--white);font-size:8.5px}
.stat.duration{background:var(--orange)}
.stat.videos{background:var(--slate)}
.stat.playlist{background:var(--blue)}
.category.spaced{margin-top:27px}
</style>
</head>
<body>

<header class="topbar">
  <div class="brand">
    <span class="brand-mark"></span>
    <span class="brand-name">brightleaf</span>
  </div>
  <div class="search">Search
    <svg width="12" height="12" viewBox="0 0 12 12"><circle cx="5" cy="5" r="3.6" fill="none" stroke="#aaa" stroke-width="1.4"/><line x1="7.7" y1="7.7" x2="11" y2="11" stroke="#aaa" stroke-width="1.6"/></svg>
  </div>
  <div class="account user">
    <span class="label">Logged in as <a href="#">ola@brightleaf.test</a></span>
    <span class="icon"><svg width="10" height="10" viewBox="0 0 10 10"><circle cx="5" cy="3" r="2.3" fill="#0b7fb6"/><path d="M1 10c0-3 1.8-4.2 4-4.2S9 7 9 10z" fill="#0b7fb6"/></svg></span>
  </div>
  <div class="account logout">
    <span class="label">Log Out</span>
    <span class="icon"><svg width="9" height="11" viewBox="0 0 9 11"><path d="M2 5V3.5a2.5 2.5 0 0 1 5 0V5" fill="none" stroke="#0b7fb6" stroke-width="1.4"/><rect x="0.5" y="5" width="8" height="6" fill="#0b7fb6"/></svg></span>
  </div>
</header>

<nav class="sidebar">
  <div class="nav-head"><span class="bullet"><svg width="14" height="12" viewBox="0 0 14 12"><path d="M1 1.5c2-.8 4-.6 6 .8v9c-2-1.2-4-1.4-6-.6zM13 1.5c-2-.8-4-.6-6 .8v9c2-1.2 4-1.4 6-.6z" fill="none" stroke="#fff" stroke-width="1.4"/></svg></span>Introduction</div>
  <div class="nav-item">Introduction</div>
  <div class="nav-head active"><span class="bullet"><svg width="13" height="13" viewBox="0 0 13 13"><path d="M6.5 1L12 3.5v6L6.5 12 1 9.5v-6z" fill="#0b7fb6"/><path d="M1 3.5L6.5 6 12 3.5M6.5 6v6" stroke="#fff" stroke-width="1" fill="none"/></svg></span>Modules</div>
  <div class="nav-item current">Our Courses</div>
  <div class="nav-item">Your Courses</div>
  <div class="nav-head"><span class="bullet"><svg width="14" height="12" viewBox="0 0 14 12"><rect x="1" y="1" width="12" height="8" fill="none" stroke="#fff" stroke-width="1.4"/><path d="M5.5 3v4l3.5-2z" fill="#fff"/><line x1="4" y1="11" x2="10" y2="11" stroke="#fff" stroke-width="1.4"/></svg></span>Playlists</div>
  <div class="nav-item">Our Courses</div>
  <div class="nav-item">Your Courses</div>
  <div class="nav-head"><span class="bullet"><svg width="13" height="13" viewBox="0 0 13 13"><path d="M2 2l9 9M11 2l-9 9" stroke="#fff" stroke-width="2.2"/></svg></span>Options</div>
  <div class="nav-item">Endre Abonnement</div>
  <div class="nav-item">Account Settings</div>
  <div class="nav-item">Contact Details</div>
</nav>

<main class="content">
  <h1 class="page-title">Our Courses</h1>

  <h2 class="category">Tavla</h2>

  <article class="course">
    <div class="course-thumb" role="img" aria-label="Screenshot of a spreadsheet with a performance table"></div>
    <div class="course-body">
      <h3 class="course-title">Example Course 1</h3>
      <p class="course-text">Lorem ipsum dolor sit amet, consectetur adipiscing elit. Quisque id ante ipsum. Morbi elementum, sapien non pretium ullamcorper, sapien lorem tempor nibh, et semper tortor eros in massa. Praesent in est non nunc aliquam vulputate. Duis molestie elit non neque mattis dignissim sit amet eu lorem. Proin sit amet tristique risus. Pellentesque vulputate scelerisque leo. Praesent quis augue vitae leo pretium congue id consectetur est. Duis id hendrerit nulla. Etiam accumsan erat non vestibulum fringilla.</p>
    </div>
    <div class="course-stats">
      <div class="stat duration"><svg width="11" height="11" viewBox="0 0 11 11"><circle cx="5.5" cy="5.5" r="4.3" fill="none" stroke="#fff" stroke-width="1.6"/><path d="M5.5 3v2.7h2" fill="none" stroke="#fff" stroke-width="1.4"/></svg>22h 35m</div>
      <div class="stat videos"><svg width="12" height="10" viewBox="0 0 12 10"><rect x="0.5" y="0.5" width="11" height="9" fill="#fff"/><rect x="3.5" y="2" width="5" height="6" fill="#3c4352"/><path d="M1.3 2h1v1h-1zM1.3 4.5h1v1h-1zM1.3 7h1v1h-1zM9.7 2h1v1h-1zM9.7 4.5h1v1h-1zM9.7 7h1v1h-1z" fill="#3c4352"/></svg>24 videos</div>
      <div class="stat playlist"><svg width="12" height="12" viewBox="0 0 12 12"><path d="M6 .5l1.7 3.6 3.8.4-2.9 2.6.9 3.9L6 9 2.5 11l.9-3.9L.5 4.5l3.8-.4z" fill="#fff"/></svg>Playlist</div>
    </div>
  </article>

  <article class="course">
    <div class="course-thumb" role="img" aria-label="Screenshot of a spreadsheet with a performance table"></div>
    <div class="course-body">
      <h3 class="course-title">Example Course 1</h3>
      <p class="course-text">Lorem ipsum dolor sit amet, consectetur adipiscing elit. Quisque id ante ipsum. Morbi elementum, sapien non pretium ullamcorper, sapien lorem tempor nibh, et semper tortor eros in massa. Praesent in est non nunc aliquam vulputate. Duis molestie elit non neque mattis dignissim sit amet eu lorem. Proin sit amet tristique risus. Pellentesque vulputate scelerisque leo. Praesent quis augue vitae leo pretium congue id consectetur est. Duis id hendrerit nulla. Etiam accumsan erat non vestibulum fringilla.</p>
    </div>
    <div class="course-stats">
      <div class="stat duration"><svg width="11" height="11" viewBox="0 0 11 11"><circle cx="5.5" cy="5.5" r="4.3" fill="none" stroke="#fff" stroke-width="1.6"/><path d="M5.5 3v2.7h2" fill="none" stroke="#fff" stroke-width="1.4"/></svg>22h 35m</div>
      <div class="stat videos"><svg width="12" height="10" viewBox="0 0 12 10"><rect x="0.5" y="0.5" width="11" height="9" fill="#fff"/><rect x="3.5" y="2" width="5" height="6" fill="#3c4352"/><path d="M1.3 2h1v1h-1zM1.3 4.5h1v1h-1zM1.3 7h1v1h-1zM9.7 2h1v1h-1zM9.7 4.5h1v1h-1zM9.7 7h1v1h-1z" fill="#3c4352"/></svg>24 videos</div>
      <div class="stat playlist"><svg width="12" height="12" viewBox="0 0 12 12"><path d="M6 .5l1.7 3.6 3.8.4-2.9 2.6.9 3.9L6 9 2.5 11l.9-3.9L.5 4.5l3.8-.4z" fill="#fff"/></svg>Playlist</div>
    </div>
  </article>

  <article class="course">
    <div class="course-thumb" role="img" aria-label="Screenshot of a spreadsheet with a performance table"></div>
    <div class="course-body">
      <h3 class="course-title">Example Course 1</h3>
      <p class="course-text">Lorem ipsum dolor sit amet, consectetur adipiscing elit. Quisque id ante ipsum. Morbi elementum, sapien non pretium ullamcorper, sapien lorem tempor nibh, et semper tortor eros in massa. Praesent in est non nunc aliquam vulputate. Duis molestie elit non neque mattis dignissim sit amet eu lorem. Proin sit amet tristique risus. Pellentesque vulputate scelerisque leo. Praesent quis augue vitae leo pretium congue id consectetur est. Duis id hendrerit nulla. Etiam accumsan erat non vestibulum fringilla.</p>
    </div>
    <div class="course-stats">
      <div class="stat duration"><svg width="11" height="11" viewBox="0 0 11 11"><circle cx="5.5" cy="5.5" r="4.3" fill="none" stroke="#fff" stroke-width="1.6"/><path d="M5.5 3v2.7h2" fill="none" stroke="#fff" stroke-width="1.4"/></svg>22h 35m</div>
      <div class="stat videos"><svg width="12" height="10" viewBox="0 0 12 10"><rect x="0.5" y="0.5" width="11" height="9" fill="#fff"/><rect x="3.5" y="2" width="5" height="6" fill="#3c4352"/><path d="M1.3 2h1v1h-1zM1.3 4.5h1v1h-1zM1.3 7h1v1h-1zM9.7 2h1v1h-1zM9.7 4.5h1v1h-1zM9.7 7h1v1h-1z" fill="#3c4352"/></svg>24 videos</div>
      <div class="stat playlist"><svg width="12" height="12" viewBox="0 0 12 12"><path d="M6 .5l1.7 3.6 3.8.4-2.9 2.6.9 3.9L6 9 2.5 11l.9-3.9L.5 4.5l3.8-.4z" fill="#fff"/></svg>Playlist</div>
    </div>
  </article>

  <h2 class="category spaced">Folio 2013</h2>

  <article class="course">
    <div class="course-thumb" role="img" aria-label="Screenshot of a spreadsheet with a performance table"></div>
    <div class="course-body">
      <h3 class="course-title">Example Course 1</h3>
      <p class="course-text">Lorem ipsum dolor sit amet, consectetur adipiscing elit. Quisque id ante ipsum. Morbi elementum, sapien non pretium ullamcorper, sapien lorem tempor nibh, et semper tortor eros in massa. Praesent in est non nunc aliquam vulputate. Duis molestie elit non neque mattis dignissim sit amet eu lorem. Proin sit amet tristique risus. Pellentesque vulputate scelerisque leo. Praesent quis augue vitae leo pretium congue id consectetur est. Duis id hendrerit nulla. Etiam accumsan erat non vestibulum fringilla.</p>
    </div>
    <div class="course-stats">
      <div class="stat duration"><svg width="11" height="11" viewBox="0 0 11 11"><circle cx="5.5" cy="5.5" r="4.3" fill="none" stroke="#fff" stroke-width="1.6"/><path d="M5.5 3v2.7h2" fill="none" stroke="#fff" stroke-width="1.4"/></svg>22h 35m</div>
      <div class="stat videos"><svg width="12" height="10" viewBox="0 0 12 10"><rect x="0.5" y="0.5" width="11" height="9" fill="#fff"/><rect x="3.5" y="2" width="5" height="6" fill="#3c4352"/><path d="M1.3 2h1v1h-1zM1.3 4.5h1v1h-1zM1.3 7h1v1h-1zM9.7 2h1v1h-1zM9.7 4.5h1v1h-1zM9.7 7h1v1h-1z" fill="#3c4352"/></svg>24 videos</div>
      <div class="stat playlist"><svg width="12" height="12" viewBox="0 0 12 12"><path d="M6 .5l1.7 3.6 3.8.4-2.9 2.6.9 3.9L6 9 2.5 11l.9-3.9L.5 4.5l3.8-.4z" fill="#fff"/></svg>Playlist</div>
    </div>
  </article>
</main>

</body>
</html>
```